Luxury 8’x4’ Acreage FOR SALE sign

I need (in 3 days) an outstanding Luxury - looking For Sale sign with my logo prominent & my brokerage logo to make up 9% of the total design space. It also needs to have “space” around it to breathe (as per brokerage qualification boundaries) It needs to be unique , have my phone number , my logo (with or without Real Estate cropped out) , brokerage logo & “for sale” or “available” or some type of wording that projects it’s a sign listing an acreage. My main focus is branding - MY logo & brand being recognized. I am unsure about including a photo of myself or not as I need this to look sleek & not busy! I have included a photo of the sign I designed & it’s just not doing it for me … I DO NOT want it to look like a business card. I’m finding it hard to make it look intentional with the DVK logo needed. It can be either logo - the box logo or the horizontal DVK logo but MUST make up 9%.
Updates

No photo of me please ! Decision made!

Target Market(s)

Luxury

Industry/Entity Type

Real Estate

Requirements
Must have
• Phone number, My logo, My Brokerage logo
Nice to have
• Needs to stand out “for sale” or “available” or

```html
<!DOCTYPE html>
<html lang="en">
<head>
<meta charset="utf-8">
<title>For Sale Sign</title>
<link href="https://fonts.googleapis.com/css2?family=Archivo+Black&family=Archivo:wght@600;800&display=swap" rel="stylesheet">
<style>
  :root {
    --page: #ffffff;
    --sign: #0b0b0b;
    --headline: #ffffff;
    --accent: #f4e27c;
    --rule: #7a7a7a;
    --badge: #6e6e6e;
    --brand: #ffffff;
  }
  html, body {
    margin: 0;
    padding: 0;
    overflow: hidden;
    background: var(--page);
  }
  .canvas {
    position: relative;
    width: 1200px;
    height: 949px;
    background: var(--page);
    overflow: hidden;
  }
  .sign {
    position: absolute;
    left: 199px;
    top: 253px;
    width: 813px;
    height: 406px;
    background: var(--sign);
  }
  .headline {
    position: absolute;
    left: 0;
    right: 0;
    top: 37px;
    margin: 0;
    text-align: center;
    font-family: "Archivo Black", "Arial Black", sans-serif;
    font-size: 130px;
    line-height: 1;
    letter-spacing: 1px;
    color: var(--headline);
  }
  .phone {
    position: absolute;
    left: 0;
    right: 0;
    top: 196px;
    display: flex;
    justify-content: center;
    align-items: center;
    gap: 16px;
    font-family: "Archivo", Arial, sans-serif;
    font-weight: 800;
    font-size: 68px;
    line-height: 1;
    color: var(--accent);
  }
  .phone-icon {
    width: 44px;
    height: 44px;
    margin-top: 6px;
  }
  .frame-rule {
    position: absolute;
    top: 207px;
    width: 140px;
    height: 152px;
  }
  .frame-rule.left { left: 48px; border-left: 3px solid var(--rule); border-bottom: 3px solid var(--rule); }
  .frame-rule.right { right: 48px; border-right: 3px solid var(--rule); border-bottom: 3px solid var(--rule); }
  .logos {
    position: absolute;
    left: 0;
    right: 0;
    top: 282px;
    height: 92px;
    display: flex;
    justify-content: center;
    align-items: center;
    gap: 26px;
  }
  .agent-brand {
    font-family: "Archivo", Arial, sans-serif;
    font-weight: 600;
    color: var(--brand);
    text-align: center;
    line-height: 1.05;
  }
  .agent-name { font-size: 36px; letter-spacing: 1px; }
  .agent-tag { font-size: 14px; letter-spacing: 7px; margin-top: 6px; }
  .brokerage-badge {
    width: 100px;
    height: 88px;
    background: var(--badge);
    display: flex;
    align-items: center;
    justify-content: center;
    font-family: "Archivo", Arial, sans-serif;
    font-weight: 600;
    font-size: 30px;
    color: var(--brand);
  }
</style>
</head>
<body>
<div class="canvas">
  <section class="sign">
    <h1 class="headline">FOR SALE</h1>
    <div class="phone">
      <svg class="phone-icon" viewBox="0 0 24 24" aria-hidden="true">
        <path fill="#f4e27c" d="M6.6 2.5c.6-.3 1.3-.1 1.6.5l1.6 3.2c.3.6.1 1.3-.4 1.6L8 8.6c.9 2.8 3.5 5.5 6.4 6.5l.9-1.4c.4-.5 1.1-.7 1.600-.4l3.2 1.6c.6.3.8 1 .5 1.6l-1 2c-.5 1-1.7 1.6-2.8 1.3C10 18.3 5.7 14 4.2 7.1 4 6 4.5 4.9 5.5 4.4z"/>
      </svg>
      <span class="phone-number">403-555-0142</span>
    </div>
    <div class="frame-rule left"></div>
    <div class="frame-rule right"></div>
    <div class="logos">
      <div class="agent-brand">
        <div class="agent-name">MARA VELDT</div>
        <div class="agent-tag">REAL ESTATE</div>
      </div>
      <div class="brokerage-badge">DVK</div>
    </div>
  </section>
</div>
</body>
</html>
```